Robotic startup business cards

We are looking for a design for a set of business cards which reflect the spirit and humor of Torvexa Robotics. We want to present ourselves as sleek, professional, but laid-back consulting company.

We primarily focus on developing robotic arms software. This software controls robots and does things like grab items, pick objects up, move them, etc.

We want to allow you maximum design creativity, but do ask that you consider our existing style guidelines (see attached files) in order to make our brand cohesive.

Target Market(s)

Startups and Mid-size robotic companies

Industry/Entity Type

Business

Contact Information for Business Card

Liam Brantly, PhD
Roboticist | Torvexa Consulting | 318.572.6094

Font styles to use
Other font styles liked:
• Source code pro

Requirements
Must have
• robots or robotic arms
• similar color scheme that works with existing brand guidelines
Nice to have
• please consider our existing style guidelines (see attached files) in order to make our brand cohesive.
• minimalism style is generally nice.
Should not have
• An old, boring, or corporate feel. Too much text.

```html
<!DOCTYPE html>
<html lang="en">
<head>
<meta charset="utf-8">
<title>Torvexa Robotics — Business Cards</title>
<link href="https://fonts.googleapis.com/css2?family=Source+Code+Pro:wght@400;500;600&display=swap" rel="stylesheet">
<style>
  :root {
    --page-bg: #ffffff;
    --card-black: #0b0d0d;
    --card-charcoal: #1a1d1e;
    --card-white: #f7f8f7;
    --brand-green: #4fc99a;
    --brand-green-deep: #1f6e52;
    --text-light: #f2f4f3;
    --text-dark: #2a2d2e;
    --shadow: rgba(0, 0, 0, 0.28);
  }
  * { box-sizing: border-box; margin: 0; padding: 0; }
  html, body {
    width: 1200px;
    height: 900px;
    overflow: hidden;
    background: var(--page-bg);
    font-family: "Source Code Pro", monospace;
  }
  .sheet {
    position: relative;
    width: 1200px;
    height: 900px;
    display: flex;
    align-items: center;
    justify-content: center;
    gap: 60px;
  }
  .card {
    position: relative;
    width: 500px;
    height: 290px;
    border-radius: 26px;
    overflow: hidden;
    box-shadow: 0 18px 30px -14px var(--shadow);
  }

  /* Front */
  .card--front {
    background: radial-gradient(ellipse at 60% 40%, var(--card-charcoal) 0%, var(--card-black) 75%);
  }
  .front-stripe {
    position: absolute;
    left: 52px;
    top: 0;
    width: 46px;
    height: 100%;
    background: rgba(255, 255, 255, 0.035);
  }
  .wordmark {
    position: absolute;
    display: flex;
    align-items: center;
    gap: 20px;
  }
  .card--front .wordmark { left: 108px; top: 118px; }
  .wordmark__square {
    width: 46px;
    height: 46px;
    border-radius: 6px;
    background: var(--brand-green);
  }
  .wordmark__name {
    font-size: 38px;
    font-weight: 400;
    letter-spacing: 0.22em;
  }
  .card--front .wordmark__name { color: var(--text-light); }

  /* Back */
  .card--back { background: var(--card-white); }
  .back-top {
    position: absolute;
    inset: 0 0 auto 0;
    height: 160px;
  }
  .card--back .wordmark { left: 70px; top: 48px; }
  .card--back .wordmark__name { color: var(--text-dark); font-size: 34px; }
  .card--back .wordmark__square { width: 42px; height: 42px; }
  .robot-hand {
    position: absolute;
    right: 18px;
    top: 22px;
    width: 74px;
    height: 132px;
    border-radius: 24px 24px 10px 10px;
    background: linear-gradient(160deg, var(--brand-green) 0%, var(--brand-green-deep) 70%, #123a2c 100%);
  }
  .accent-line {
    position: absolute;
    left: 0;
    right: 0;
    top: 154px;
    height: 10px;
    background: var(--brand-green);
  }
  .back-bottom {
    position: absolute;
    left: 0;
    right: 0;
    top: 164px;
    bottom: 0;
    background: radial-gradient(ellipse at 50% 20%, var(--card-charcoal) 0%, var(--card-black) 80%);
    text-align: center;
    padding-top: 18px;
  }
  .contact__name {
    color: var(--brand-green);
    font-size: 17px;
    font-weight: 500;
    letter-spacing: 0.12em;
  }
  .contact__degree { font-size: 11px; letter-spacing: 0.05em; }
  .contact__role,
  .contact__company {
    color: var(--text-light);
    font-size: 10px;
    letter-spacing: 0.08em;
    line-height: 1.35;
  }
  .contact__role { margin-top: 3px; }
  .contact__phone {
    color: var(--text-light);
    font-size: 17px;
    font-weight: 500;
    letter-spacing: 0.06em;
    margin-top: 22px;
  }
</style>
</head>
<body>
  <main class="sheet">
    <section class="card card--front" aria-label="Card front">
      <div class="front-stripe"></div>
      <div class="wordmark">
        <span class="wordmark__square"></span>
        <span class="wordmark__name">TORVEXA</span>
      </div>
    </section>

    <section class="card card--back" aria-label="Card back">
      <div class="back-top">
        <div class="wordmark">
          <span class="wordmark__square"></span>
          <span class="wordmark__name">TORVEXA</span>
        </div>
        <div class="robot-hand" role="img" aria-label="Green metallic robotic hand raised upright"></div>
      </div>
      <div class="accent-line"></div>
      <div class="back-bottom">
        <p class="contact__name">LIAM BRANTLY,<span class="contact__degree">PHD</span></p>
        <p class="contact__role">ROBOTICIST</p>
        <p class="contact__company">TORVEXA CONSULTING</p>
        <p class="contact__phone">318.572.6094</p>
      </div>
    </section>
  </main>
</body>
</html>
```